Film Poster Design For Japanese Film Poster #2

The title of this colour film is KAZE YAMA TSUKI HOSHI春 夏 秋 冬Translated this is literallySpring Summer Fall Winter ... however the English title is FOUR SEASONSWe attached a series of screen shots from the film and also the computer generated Kanji characters. We will be updating the brief with the Japanese title characters which currently being hand painted.We require the post in two formats. One being the traditional poster format and the other being in a wide screen ration of 1000px by 465px. Same design.This is a drama, feature length film comprising of four separate stories. The is mixture of Japanese and English dialogue. We are looking at 2 possible designs. You can choose to submit either.1: A with lots of white space ... focussing on smaller images at the Japanese text. I have uploaded a sample poster as a very rough indication. "Stories nobody ever wrote down about the quiet ones" / "Odile Bettina Rue Ingrid" - Lots of white space.Ideally we would have liked to have had the image of the young girl in the kimono pulling on the bell rope clear cut and used on white as a single main image. However, we are not sure that the clarity or resolution of the original image is sufficient. 2: One with lots of images as you can see with the two "Bridge Of Dust" Sample posters.Obviously we are not looking for a copy of either poster, but these posters are a guide to the two looks we are after.Thanks. Kaede
Hello all,Apologies for the delay. We have had to work through some naming issues.The film's English title has had to be renamed to THE LANTERNS. Please do not used TEN LANTERNS in any designed moving forward.Thanks Kaede Added Sunday, May 25, 2014

```html
<!DOCTYPE html>
<html lang="en">
<head>
<meta charset="utf-8">
<title>THE LANTERNS — Film Poster</title>
<link rel="stylesheet" href="https://fonts.googleapis.com/css2?family=Yuji+Syuku&family=Oswald:wght@200;300;400&display=swap">
<style>
  :root {
    --paper: #ffffff;
    --ink: #111111;
    --ink-soft: #3a3a3a;
    --ink-wash: #5c5c5c;
    --kimono-red: #b8283c;
    --credit-grey: #555555;
  }
  * { margin: 0; padding: 0; box-sizing: border-box; }
  html, body {
    width: 800px;
    height: 1200px;
    overflow: hidden;
    background: var(--paper);
  }
  .poster {
    position: relative;
    width: 800px;
    height: 1200px;
    background: var(--paper);
    color: var(--ink);
    font-family: "Oswald", sans-serif;
  }
  .kanji-title {
    position: absolute;
    top: 92px;
    left: 0;
    width: 100%;
    text-align: center;
    font-family: "Yuji Syuku", serif;
    font-size: 60px;
    letter-spacing: 10px;
    color: var(--ink);
  }
  .brush-artwork {
    position: absolute;
    top: 190px;
    left: 140px;
    width: 530px;
    height: 680px;
    background:
      radial-gradient(ellipse 22% 30% at 50% 42%, var(--kimono-red) 0%, rgba(184,40,60,0.5) 45%, transparent 75%),
      radial-gradient(ellipse 50% 48% at 50% 50%, var(--ink) 0%, var(--ink-soft) 45%, rgba(92,92,92,0.35) 75%, rgba(255,255,255,0) 100%);
  }
  .title-block {
    position: absolute;
    top: 872px;
    left: 0;
    width: 100%;
    text-align: center;
    color: var(--ink);
  }
  .title-lead {
    display: block;
    font-weight: 200;
    font-size: 74px;
    line-height: 1;
    letter-spacing: 4px;
  }
  .title-main {
    display: block;
    margin-top: 4px;
    font-weight: 300;
    font-size: 30px;
    letter-spacing: 3px;
  }
  .credits {
    position: absolute;
    top: 1018px;
    left: 0;
    width: 100%;
    text-align: center;
    color: var(--credit-grey);
    font-weight: 300;
    text-transform: uppercase;
    line-height: 1.5;
  }
  .credit-line { display: block; font-size: 11px; letter-spacing: 0.6px; }
  .credit-line.lead { font-size: 12px; }
  .credit-line.release { font-size: 13px; font-weight: 400; margin-top: 4px; color: var(--ink); }
  .credit-line.legal { font-size: 8px; margin-top: 4px; }
</style>
</head>
<body>
  <main class="poster">
    <h2 class="kanji-title" lang="ja">風山月星</h2>

    <div class="brush-artwork" role="img"
         aria-label="Large hand-painted black ink brush kanji with splatter, framing a photo of a young girl in a red and navy kimono pulling a temple bell rope"></div>

    <h1 class="title-block">
      <span class="title-lead">THE</span>
      <span class="title-main">LANTERNS</span>
    </h1>

    <section class="credits">
      <span class="credit-line lead">A Northwind Pictures film in association with Lantern House</span>
      <span class="credit-line">Written and directed by Kaede Mori produced by Aya Sato and Ren Ito</span>
      <span class="credit-line">Starring Mika Ono Yuki Hara Sora Kimura Taku Noda</span>
      <span class="credit-line">Music by Hana Ishii edited by Ken Abe photography by Jun Mori</span>
      <span class="credit-line">Costumes by Rin Ota sound by Dai Kondo</span>
      <span class="credit-line release">Coming Soon</span>
      <span class="credit-line legal">Copyright Northwind Pictures all rights reserved</span>
    </section>
  </main>
</body>
</html>
```